logo rebuild / business card for kestravonworks

Hello Sir,
(We have already worked together, for one party who i invited)
Can you make the logo in attachment better? I want more 3D feeling with colors. Also in little format that i can put it on my business card. For better understanding of my work, look in google : "diamond cut cnc lathe" or "diamond cut finish alloy wheels"

Or if you have a better idea you can start from scratch.
Thank,
Rik

Target Market(s)

automotive repair market

Industry/Entity Type

Business

Contact Information for Business Card

name company : Brellmor Solutions
Manager : Rik D. Vannoorde
Street : Rue des peupliers anciens 4
city and code : B7813 VELDMORE-OSTAL
Cellphone : +32 471 586 304
Web : www.kestravonworks.com
email : rik@kestravonworks.com

Requirements
Must have
• seraparte logo file in cmjn 300dpi 1/4 scale jpeg
Nice to have
• 3D look something shiny classy

```html
<!DOCTYPE html>
<html lang="en">
<head>
<meta charset="utf-8">
<title>Kestravonworks business card</title>
<link href="https://fonts.googleapis.com/css2?family=Roboto+Condensed:wght@400;700&display=swap" rel="stylesheet">
<style>
  :root {
    --page: #e9e9e7;
    --card-white: #f4f5f6;
    --band-black: #111214;
    --band-edge: #9a9ca0;
    --panel-dark: #222326;
    --panel-dark-2: #17181a;
    --ice-blue: #8fd3ee;
    --text-light: #e8e8e8;
    --text-muted: #a9abad;
    --photo-dark: #1e1c1a;
    --photo-mid: #5e5246;
    --photo-light: #8d8c8a;
  }
  * { box-sizing: border-box; margin: 0; padding: 0; }
  html, body { width: 1200px; height: 800px; overflow: hidden; }
  body {
    background: var(--page);
    font-family: "Roboto Condensed", "Arial Narrow", sans-serif;
    display: flex; align-items: center; justify-content: center; gap: 40px;
  }
  .card {
    position: relative; width: 540px; height: 310px; overflow: hidden;
    box-shadow: 0 10px 30px rgba(0,0,0,.18);
  }
  .card-front { background: var(--card-white); }
  .card-front .bands { position: absolute; inset: 0; }
  .front-logo {
    position: absolute; left: 50%; top: 50%; transform: translate(-50%, -50%);
    display: flex; align-items: center; gap: 10px;
  }
  .logo-mark { width: 16px; height: 16px; background: var(--ice-blue); flex: none; }
  .logo-name {
    font-weight: 700; font-size: 26px; letter-spacing: 1px;
    text-transform: uppercase; color: #1c1d20; white-space: nowrap;
  }
  .card-back { background: linear-gradient(160deg, var(--panel-dark), var(--panel-dark-2)); }
  .wheel-photo {
    position: absolute; left: 0; top: 0; width: 215px; height: 100%;
    background: radial-gradient(circle at 55% 55%, var(--photo-light) 0%, #1b1b1c 45%, var(--photo-dark) 65%, var(--photo-mid) 100%);
  }
  .divider {
    position: absolute; left: 215px; top: 0; width: 5px; height: 100%;
    background: var(--band-edge);
  }
  .info { position: absolute; left: 245px; top: 24px; right: 20px; }
  .back-logo { display: flex; align-items: center; gap: 8px; }
  .info .logo-name { color: var(--ice-blue); font-size: 18px; }
  .info .logo-mark { width: 12px; height: 12px; }
  .person-name {
    margin-top: 26px; font-weight: 700; font-size: 24px; line-height: 1.1;
    color: var(--ice-blue); white-space: nowrap;
  }
  .person-role { font-size: 14px; color: var(--text-muted); margin-bottom: 14px; }
  .contact-list { list-style: none; }
  .contact-list li {
    display: flex; align-items: center; gap: 10px;
    font-size: 14px; color: var(--text-light); height: 22px; white-space: nowrap;
  }
  .contact-icon {
    width: 18px; height: 18px; background: var(--ice-blue);
    display: flex; align-items: center; justify-content: center; flex: none;
  }
  .contact-icon.blank { background: transparent; }
</style>
</head>
<body>
  <section class="card card-front">
    <svg class="bands" width="540" height="310" viewBox="0 0 540 310">
      <polygon points="0,0 120,0 88,310 0,310" fill="var(--band-black)"/>
      <line x1="130" y1="0" x2="98" y2="310" stroke="var(--band-edge)" stroke-width="3"/>
      <polygon points="420,0 540,0 540,310 452,310" fill="var(--band-black)"/>
      <line x1="410" y1="0" x2="442" y2="310" stroke="var(--band-edge)" stroke-width="3"/>
    </svg>
    <div class="front-logo">
      <span class="logo-mark"></span>
      <span class="logo-name">Kestravonworks</span>
    </div>
  </section>

  <section class="card card-back">
    <div class="wheel-photo" role="img" aria-label="Photo of a diamond cut black alloy wheel"></div>
    <div class="divider"></div>
    <div class="info">
      <div class="back-logo">
        <span class="logo-mark"></span>
        <span class="logo-name">Kestravonworks</span>
      </div>
      <h1 class="person-name">Rik D. Vannoorde</h1>
      <p class="person-role">Manager</p>
      <ul class="contact-list">
        <li><span class="contact-icon"><svg width="12" height="12" viewBox="0 0 12 12"><path d="M3 1h2l1 3-1.5 1a6 6 0 0 0 2.5 2.5L8 6l3 1v2a2 2 0 0 1-2 2A8 8 0 0 1 1 3a2 2 0 0 1 2-2z" fill="#1c1d20"/></svg></span>+32 471 586 304</li>
        <li><span class="contact-icon"><svg width="12" height="10" viewBox="0 0 12 10"><rect x="0.5" y="0.5" width="11" height="9" fill="none" stroke="#1c1d20"/><path d="M0.5 0.5 6 5.5 11.5 0.5" fill="none" stroke="#1c1d20"/></svg></span>rik@kestravonworks.com</li>
        <li><span class="contact-icon"><svg width="10" height="12" viewBox="0 0 10 12"><path d="M5 12S0 6.5 0 4.5a5 5 0 0 1 10 0C10 6.5 5 12 5 12z" fill="#1c1d20"/><circle cx="5" cy="4.5" r="1.7" fill="var(--ice-blue)"/></svg></span>Rue des peupliers anciens 4</li>
        <li><span class="contact-icon"><svg width="12" height="12" viewBox="0 0 12 12"><circle cx="6" cy="6" r="5.3" fill="none" stroke="#1c1d20"/><ellipse cx="6" cy="6" rx="2.3" ry="5.3" fill="none" stroke="#1c1d20"/><line x1="0.7" y1="6" x2="11.3" y2="6" stroke="#1c1d20"/></svg></span>www.kestravonworks.com</li>
        <li><span class="contact-icon blank"></span>city and code : B7813 VELDMORE-OSTAL</li>
      </ul>
    </div>
  </section>
</body>
</html>
```